Business Card design for an International Import Export House

We need a Business Card design for our import export business. We trade in Minerals, Metals, Rice, Sugar, Steel etc.. The design should be minimalistic. It may or may not contain the physical address. In case you want to include the physical address - 418 Verandah Heights, Marlow Sector 9, Gurgaon, Haryana, India, 122009.

Target Market(s)

Steel Mills or Steel Plants, Factories, Mining businesses, Industrial houses, Government Agencies

Industry/Entity Type

Importer

Contact Information for Business Card

Business Name - Marovin Overseas

Font styles to use
Other font styles liked:
• montserrat

Requirements
Must have
• Ravi Kandola - President
• www.marovinoverseas.com
• ravi@marovinoverseas.com
• +91-987-654-3217
Nice to have
• worldwide suppliers of ores

```html
<!DOCTYPE html>
<html lang="en">
<head>
<meta charset="utf-8">
<title>Marovin Overseas – Business Card</title>
<link rel="stylesheet" href="https://fonts.googleapis.com/css2?family=Montserrat:wght@400;800;900&family=Roboto:wght@400&display=swap">
<style>
  :root {
    --teal: #3a93ad;
    --teal-dark: #2f7f97;
    --ink: #151515;
    --ink-soft: #2a2a2a;
    --paper: #f4f4f2;
    --backdrop: #e9ecee;
  }
  * { box-sizing: border-box; margin: 0; padding: 0; }
  html, body {
    width: 1200px;
    height: 873px;
    overflow: hidden;
    background: var(--backdrop);
  }
  .canvas {
    width: 1200px;
    height: 873px;
    display: flex;
    align-items: center;
    justify-content: center;
    gap: 44px;
  }
  .card {
    position: relative;
    width: 540px;
    height: 309px;
    background: var(--paper);
    box-shadow: 0 10px 28px rgba(0,0,0,0.14), 0 2px 5px rgba(0,0,0,0.08);
    overflow: hidden;
  }

  /* Front */
  .card-front__band {
    position: absolute;
    left: 0; top: 0; bottom: 0;
    width: 180px;
    background: var(--teal);
    display: flex;
    align-items: center;
    justify-content: center;
  }
  .brand-mark {
    display: flex;
    flex-direction: column;
    align-items: center;
    gap: 10px;
  }
  .brand-mark__dot {
    width: 22px; height: 22px;
    border-radius: 50%;
    background: #fff;
  }
  .brand-mark__name {
    font-family: "Montserrat", sans-serif;
    font-weight: 800;
    font-size: 13px;
    letter-spacing: 0.06em;
    text-transform: uppercase;
    color: #fff;
    text-align: center;
    line-height: 1.35;
  }
  .card-front__person {
    position: absolute;
    right: 34px;
    top: 40px;
    text-align: right;
  }
  .person__name {
    font-family: "Montserrat", sans-serif;
    font-weight: 900;
    font-size: 27px;
    color: var(--ink);
    letter-spacing: 0.01em;
  }
  .person__title {
    font-family: "Montserrat", sans-serif;
    font-weight: 400;
    font-size: 17px;
    color: var(--ink-soft);
    margin-top: 2px;
  }
  .card-front__contact {
    position: absolute;
    left: 206px;
    bottom: 38px;
    list-style: none;
    font-family: "Roboto", sans-serif;
    font-size: 15px;
    line-height: 1.55;
    color: var(--ink);
    letter-spacing: 0.02em;
  }

  /* Back */
  .card-back__edge {
    position: absolute;
    left: 0; right: 0; top: 0;
    height: 9px;
    background: var(--teal);
  }
  .card-back__brand {
    position: absolute;
    inset: 9px 0 0 0;
    display: flex;
    align-items: center;
    justify-content: center;
    gap: 18px;
  }
  .card-back__name {
    font-family: "Montserrat", sans-serif;
    font-weight: 800;
    font-size: 30px;
    letter-spacing: 0.02em;
    text-transform: uppercase;
    color: var(--teal-dark);
  }
  .card-back__dot {
    width: 30px; height: 30px;
    border-radius: 50%;
    background: var(--teal);
  }
</style>
</head>
<body>
<main class="canvas">
  <section class="card card-front" aria-label="Business card front">
    <div class="card-front__band">
      <div class="brand-mark">
        <span class="brand-mark__dot"></span>
        <span class="brand-mark__name">Marovin<br>Overseas</span>
      </div>
    </div>
    <div class="card-front__person">
      <p class="person__name">Ravi Kandola</p>
      <p class="person__title">President</p>
    </div>
    <ul class="card-front__contact">
      <li>T: +91-987-654-3217</li>
      <li>M: ravi@marovinoverseas.com</li>
      <li>W: www.marovinoverseas.com</li>
    </ul>
  </section>

  <section class="card card-back" aria-label="Business card back">
    <div class="card-back__edge"></div>
    <div class="card-back__brand">
      <span class="card-back__name">Marovin Overseas</span>
      <span class="card-back__dot"></span>
    </div>
  </section>
</main>
</body>
</html>
```